VLK IT Solutions Provider

Please read attached documentation completely before beginning Project. Thank you!

Folio Nest Project Requirements

Thank you for your interest in this design contest. We are always welcome to questions and are looking forward to seeing what you can come up with.

The logo is located on the current site homepage http://www.vantolirex.com/

Bootstrap

We work on a Bootstrap platform with our custom built CMS. We require all designs to be

sized accordingly with the bootstrap grid system found here: http://trelvanix.com/css/#grid

Start of Competition Requirements

At the start of a competition, we are looking for general Home Page Design concepts and interior page design concepts as well.

HOME PAGE DESIGN

Any changes requested by the client in the original designs

Responsive Tablet View (using standard bootstrap media queries, we need to see an

example of a tablet size home page view)

Responsive Phone View (using standard bootstrap media queries, we need to see an

example of a phone size home page view)

INTERIOR PAGE DESIGN

These pages are general content pages. Our CMS allows for the creation of unlimited

pages and gives the client control of adding them. Interior Page Designs can be built

with 1 column, 2 columns (either right side bar or left sidebar)

Examples of buttons and button states,

Examples of drop down menus

Examples of H1 through H5 plus body copy

We uploaded a clean logo to use on the project. Thank you.

Project Deadline Extended

We added a updated Creative Brief document to help out. Please take a look thanks!

```html
<!DOCTYPE html>
<html lang="en">
<head>
<meta charset="utf-8">
<title>VLK – Technology Solutions</title>
<link href="https://fonts.googleapis.com/css2?family=Open+Sans:wght@400;600&display=swap" rel="stylesheet">
<style>
  :root {
    --bg: #000000;
    --navy: #020f3a;
    --navy-deep: #010a2a;
    --blue: #0a3fd6;
    --blue-bright: #1d4fe8;
    --link: #2f63ff;
    --nav-blue: #0e4a9c;
    --nav-active: #1c63c0;
    --white: #ffffff;
    --gold: #e8b21b;
  }
  * { margin: 0; padding: 0; box-sizing: border-box; }
  html, body { width: 1200px; height: 1000px; overflow: hidden; background: var(--bg); }
  body { position: relative; font-family: "Open Sans", sans-serif; color: var(--white); }

  .brand { position: absolute; left: 118px; top: 28px; display: flex; align-items: center; gap: 10px; }
  .brand-mark { width: 22px; height: 22px; border-radius: 50%; background: var(--blue); }
  .brand-name { font-size: 40px; font-weight: 600; color: var(--blue-bright); letter-spacing: 1px; }

  .search { position: absolute; left: 889px; top: 13px; width: 206px; height: 30px; background: #f2f2f2; border-radius: 6px; display: flex; align-items: center; }
  .search-field { flex: 1; font-size: 10px; color: #555; padding-left: 10px; }
  .search-btn { width: 38px; height: 100%; border-left: 2px solid #333; display: flex; align-items: center; justify-content: center; }

  .main-nav { position: absolute; left: 125px; top: 103px; width: 942px; height: 37px;
    background: linear-gradient(90deg, rgba(14,74,156,0) 0%, var(--nav-blue) 12%, var(--nav-blue) 88%, rgba(14,74,156,0) 100%); }
  .main-nav ul { list-style: none; position: absolute; left: 151px; top: 0; display: flex; height: 100%; border-left: 1px solid #0a2a5c; }
  .main-nav li { height: 100%; display: flex; align-items: center; justify-content: center; font-size: 15.5px; border-right: 1px solid #0a2a5c; }
  .main-nav li.active { background: var(--nav-active); }

  .hero { position: absolute; left: 137px; top: 140px; width: 905px; height: 272px;
    background: linear-gradient(90deg, rgba(3,20,55,0) 0%, #05224f 12%, #0a2c5c 45%, #6f8cae 70%, #b9c7d8 85%, rgba(20,50,90,0) 100%); }
  .hero-title { position: absolute; left: 150px; top: 76px; width: 330px; text-align: center; font-size: 20.5px; line-height: 24px; }

  .welcome-title { position: absolute; left: 106px; top: 480px; font-size: 26px; font-weight: 400; color: var(--blue-bright); }
  .welcome-text { position: absolute; left: 142px; top: 528px; width: 710px; font-size: 12px; line-height: 17.5px; }

  .partners { position: absolute; left: 106px; top: 713px; width: 732px; height: 40px; }
  .arrow { position: absolute; top: 0; width: 37px; height: 37px; }
  .badge { position: absolute; background: #e9ecf2; }

  .careers { position: absolute; left: 929px; top: 444px; width: 169px; height: 306px; background: var(--navy); }
  .careers-head { height: 48px; background: linear-gradient(100deg, var(--blue) 0%, #2a55e8 100%); clip-path: polygon(0 0, 100% 6%, 100% 100%, 0 92%); padding: 10px 0 0 16px; font-size: 20px; }
  .careers ul { list-style: none; padding: 21px 0 0 22px; }
  .careers li { font-size: 12px; line-height: 23.3px; color: var(--link); }

  .footer { position: absolute; left: 99px; top: 917px; width: 1000px; height: 83px; background: var(--navy-deep); }
  .footer-nav { position: absolute; left: 18px; top: 10px; display: flex; gap: 26px; font-size: 10.5px; list-style: none; }
  .footer-contact { position: absolute; left: 835px; top: 12px; font-size: 12px; line-height: 14px; }
  .copyright { position: absolute; left: 0; width: 100%; top: 65px; text-align: center; font-size: 10.5px; }
</style>
</head>
<body>
  <header>
    <div class="brand"><span class="brand-mark"></span><span class="brand-name">VLK</span></div>
    <div class="search">
      <span class="search-field">Search Here. . . .</span>
      <span class="search-btn">
        <svg width="18" height="18" viewBox="0 0 18 18"><circle cx="7" cy="7" r="5" fill="none" stroke="#333" stroke-width="2"/><line x1="11" y1="11" x2="16" y2="16" stroke="#333" stroke-width="3"/></svg>
      </span>
    </div>
    <nav class="main-nav">
      <ul>
        <li class="active" style="width:87px">HOME</li>
        <li style="width:120px">ABOUT VLK</li>
        <li style="width:110px">DIVISIONS</li>
        <li style="width:117px">PRODUCTS</li>
        <li style="width:107px">SERVICES</li>
        <li style="width:101px">CONTACT</li>
      </ul>
    </nav>
  </header>

  <section class="hero" role="img" aria-label="Scientists in lab coats examining a sample at a computer workstation">
    <h1 class="hero-title" style="font-weight:400">Technology Solutions<br>For<br>National Defense &amp; Global Security</h1>
  </section>

  <main>
    <h2 class="welcome-title">Welcome</h2>
    <p class="welcome-text">Since 1988, Vantolirex Research Corporation has been providing innovative and cost-effective products and services to customers worldwide. We are a vital source for leading-edge technology solutions that help our customers respond to opportunities faster, achieve more from their operations, and exceed their requirements.</p>

    <div class="partners">
      <svg class="arrow" style="left:0" viewBox="0 0 37 37"><circle cx="18.5" cy="18.5" r="17" fill="none" stroke="#1d3fd6" stroke-width="2"/><path d="M9 18.5 L26 10 L21 18.5 L26 27 Z" fill="#1d3fd6"/></svg>
      <div class="badge" style="left:85px;top:-2px;width:62px;height:39px"></div>
      <div class="badge" style="left:222px;top:-9px;width:62px;height:54px;border-radius:50%;background:#8a95a8"></div>
      <div class="badge" style="left:377px;top:-5px;width:133px;height:50px"></div>
      <div class="badge" style="left:595px;top:-5px;width:44px;height:48px;background:#2a3f9a"></div>
      <svg class="arrow" style="left:695px" viewBox="0 0 37 37"><circle cx="18.5" cy="18.5" r="17" fill="none" stroke="#1d3fd6" stroke-width="2"/><path d="M28 18.5 L11 10 L16 18.5 L11 27 Z" fill="#1d3fd6"/></svg>
    </div>
  </main>

  <aside class="careers">
    <div class="careers-head">We’re hiring</div>
    <ul>
      <li>A Career at VLK</li>
      <li>Benefits</li>
      <li>Corporate Culture</li>
      <li>How to Apply</li>
      <li>Job Search</li>
      <li>Recruiting Events</li>
      <li>Our Hiring Process</li>
      <li>Diversity</li>
      <li>Student Opportunities</li>
      <li>EEO is the Law</li>
    </ul>
  </aside>

  <footer class="footer">
    <ul class="footer-nav">
      <li>HOME</li><li>ABOUT VLK</li><li>DIVISIONS</li><li>PRODUCTS</li><li>SERVICES</li><li>CONTACT</li>
    </ul>
    <address class="footer-contact" style="font-style:normal">(555) 214-7380<br>1480 Harlow Crest Drive,<br>Suite 210 North<br>Brenton, GA 30412</address>
    <p class="copyright">© Vantolirex Research Corporation</p>
  </footer>
</body>
</html>
```